Quite like thee: needs a logo design and a business card

The business name is called: Quite like thee. It's all about fashion for everyone who needs to gain confidence and find his own style: Image Consultant, Personal Shopper. Here my Facebook fan page: https://www.facebook.com/pages/Quite-like-thee/318264907152839

I would like a smart logo & business card. The design has to be smart and long lasting. I like simplicity ("less is more"). The image needs to bring over seriousness and style. I target people from 35-65 years old. I would love to have smart warm colours like brown mole or anthracite, eventually with some berry or bordeaux red.

The copy is the following:
Quite like thee
Doreen Pavlik
Mobile: +27 72 463 08 29
eMail: pavlik.doreen@brightmailbox.net
Cape Town

Reason: I'm not in a rush.

Target Market(s)

Core target group: 35-65 years old women; wealthy; living in Cape Town
Larger target group: South Africa; eventually men too

Industry/Entity Type

Business

```html
<!DOCTYPE html>
<html lang="en">
<head>
<meta charset="utf-8">
<title>Quite like thee – business card</title>
<link rel="stylesheet" href="https://fonts.googleapis.com/css2?family=Alegreya:ital,wght@1,400&display=swap">
<style>
  :root {
    --backdrop: #e5e5e5;
    --berry: #8e0073;
    --rose: #b13c5a;
    --amber: #d2702f;
    --gold: #f7c600;
    --paper: #ffffff;
    --script: "Alegreya", Georgia, serif;
  }
  * { margin: 0; padding: 0; box-sizing: border-box; }
  html, body {
    width: 1200px;
    height: 1200px;
    overflow: hidden;
    background: var(--backdrop);
  }
  .sheet {
    position: relative;
    width: 1200px;
    height: 1200px;
  }
  .card {
    position: absolute;
    left: 175px;
    width: 850px;
    height: 472px;
    overflow: hidden;
    font-family: var(--script);
    font-style: italic;
    font-weight: 400;
  }
  .card--front {
    top: 103px;
    background: linear-gradient(to bottom,
      var(--berry) 0%,
      var(--berry) 44%,
      var(--rose) 60%,
      var(--amber) 78%,
      var(--gold) 100%);
  }
  .card--back {
    top: 624px;
    background: var(--paper);
  }

  /* brand mark: plain circle with the business name */
  .brand-mark {
    position: absolute;
    left: 560px;
    top: 150px;
    width: 250px;
    display: flex;
    flex-direction: column;
    align-items: center;
    gap: 18px;
  }
  .brand-mark__dot {
    width: 64px;
    height: 64px;
    border-radius: 50%;
  }
  .brand-mark__name {
    font-size: 32px;
    line-height: 1;
    white-space: nowrap;
  }
  .card--front .brand-mark { top: 120px; }
  .card--front .brand-mark__dot { background: var(--gold); }
  .card--front .brand-mark__name { color: var(--gold); }
  .card--back .brand-mark__dot { background: var(--berry); }
  .card--back .brand-mark__name { color: var(--berry); }

  .front-tagline,
  .front-name {
    position: absolute;
    left: 125px;
    width: 400px;
    text-align: center;
    color: var(--paper);
    white-space: nowrap;
    line-height: 1;
  }
  .front-tagline {
    top: 248px;
    font-size: 46px;
  }
  .front-name {
    top: 396px;
    font-size: 35px;
  }
  .card--front .brand-mark { left: 580px; }

  .contact {
    position: absolute;
    left: 41px;
    top: 285px;
    list-style: none;
    color: var(--berry);
    font-size: 24px;
    line-height: 30px;
    white-space: nowrap;
  }
</style>
</head>
<body>
  <main class="sheet">
    <section class="card card--front">
      <p class="front-tagline">Quite like thee</p>
      <p class="front-name">Doreen Pavlik</p>
      <div class="brand-mark">
        <span class="brand-mark__dot"></span>
        <span class="brand-mark__name">Quite like thee</span>
      </div>
    </section>

    <section class="card card--back">
      <div class="brand-mark">
        <span class="brand-mark__dot"></span>
        <span class="brand-mark__name">Quite like thee</span>
      </div>
      <ul class="contact">
        <li class="contact__business">Quite like thee</li>
        <li class="contact__name">Doreen Pavlik</li>
        <li class="contact__phone">Mobile: +27 72 463 08 29</li>
        <li class="contact__email">eMail: pavlik.doreen@brightmailbox.net</li>
        <li class="contact__city">Cape Town</li>
      </ul>
    </section>
  </main>
</body>
</html>
```